Stationery Design Project

We need a stationery design for our Norwegian trucking company. We have existed for about 15 years and our 12 drivers uses relatively new vehicles to transport goods around in northern Norway. Long distance routes with fresh fish og food transport is our main operations.

We have already made alogo that's printed on our trucks. The logo and a picture of our trucks is attached. I think the logo i crappy, but since its already in use, changing it is not an option in this round. Still using a better colour scheme in the overall stationery and more interesting fonts is possible (altso in the logo).

Company details:
Name: Vikstrandbil AS
Organisation nr 981 537 608
Post adress: 8613 Lysvær

I like minimalism and simplicity. I am avalibly for questions in normal GMT working hours either here or on mail: petter@vikstrand.no

Reason: Hi. Im extending the deadline because I needed some time to find a vector file of our logo. Sorry for the inconvenience

Hi, and thanks for all your interest in the project. Some updates:

-          I have decided to commit to using one of the designs. Some designer will get the payment.

-          I have extended the deadline with 24 hours since I needed some time to find our firms vector logo (a slow Swedish man was holding me up)

-          We will not choose a design before the deadline. No need to rush.

-          We have received a lot of great design and think there is a need to specified the product we want to make:

o   Business Card for all our employers. I just need the design and will duplicate with the correct numbers and name myself. The information on should be: Logo, employer’s name, Phone number, email, website, Postal number and address. Use this as a template: logo, Leif Brattli, 47283916, Leif@vikstrand.no,, vikstrand.no, 8613 Lysvær. The order and placement of the information is your creative decision.

o   Stickers to put on the goods we travel. On the sticker the should be the following information: Logo, phone number, Tekst and link: Fraktæ av Vikstrandbil. Ke du syns? Vikstrand.no/tilbakemelding (this means: Handled by Vikstrandbil. What do you think Vikstrand.no/feedback -à the link will be a feedback form). The placement the information and size is your creative decision with some stings: we have been thinking of using Prentavo for printing and see that a size about 6x6 cm, 8x5 or something like that. (with 3000 copies our budget is 200 punds). Any suggestions of other suppliers are welcome. Prentavo price calculator http://www.prentavoprint.co.uk/digital-litho-printing/printing-labels-tags/stickers/

o   Letterhead with logo, address, phone number and organizational number.

o   Envelopes with logo,address, phone number and organizational number.

Have a nice day.

 

 

• Using the blue colour in the logo and using a similar graphic approch.

```html
<!DOCTYPE html>
<html lang="no">
<head>
<meta charset="utf-8">
<title>Vikstrandbil – stationery</title>
<link rel="stylesheet" href="https://fonts.googleapis.com/css2?family=Montserrat:ital,wght@0,400;0,600;0,700;1,700&display=swap">
<style>
  :root {
    --backdrop: #b6d8ef;
    --paper: #ffffff;
    --brand: #1b3f9e;
    --navy: #1f2a78;
    --label: #5a52a6;
    --value: #555a66;
    --band: #a4c6e7;
    --stamp: #1f6f78;
    --shadow: 0 4px 10px rgba(40, 70, 100, 0.28);
  }
  * { box-sizing: border-box; margin: 0; padding: 0; }
  html, body { width: 1200px; height: 1000px; overflow: hidden; }
  body {
    position: relative;
    background: var(--backdrop);
    font-family: "Montserrat", Arial, sans-serif;
    color: var(--value);
  }
  .sheet { position: absolute; background: var(--paper); box-shadow: var(--shadow); }

  .wordmark {
    display: inline-flex; align-items: center; gap: 6px;
    color: var(--brand); font-weight: 700; letter-spacing: -0.5px; line-height: 1;
  }
  .wordmark .dot { border-radius: 50%; background: var(--brand); flex: none; }

  .label { color: var(--label); }
  .company { color: var(--navy); font-weight: 700; }

  /* Letterhead */
  .letterhead { left: 71px; top: 76px; width: 595px; height: 842px; }
  .letterhead .wordmark { position: absolute; top: 38px; left: 0; right: 0; justify-content: center; font-size: 30px; }
  .letterhead .wordmark .dot { width: 14px; height: 14px; }
  .letterhead .footer {
    position: absolute; left: 0; right: 0; top: 760px;
    text-align: center; font-size: 10px; line-height: 13px;
  }
  .letterhead .footer .company { font-size: 10px; margin-bottom: 7px; }

  /* Business card */
  .business-card {
    left: 732px; top: 126px; width: 245px; height: 156px;
    transform: rotate(6.6deg); text-align: center;
  }
  .business-card .wordmark { margin-top: 26px; font-size: 23px; }
  .business-card .wordmark .dot { width: 11px; height: 11px; }
  .business-card .name { color: var(--navy); font-weight: 700; font-size: 11px; margin-top: 22px; }
  .business-card .details { font-size: 9.5px; line-height: 12px; margin-top: 12px; }

  /* Sticker */
  .sticker {
    left: 717px; top: 350px; width: 227px; height: 141px;
    border-radius: 7px; overflow: hidden; text-align: center;
  }
  .sticker .wordmark { margin-top: 16px; font-size: 19px; }
  .sticker .wordmark .dot { width: 9px; height: 9px; }
  .sticker .band {
    position: absolute; left: 0; right: 0; top: 53px; height: 58px;
    background: var(--band); padding-top: 3px;
  }
  .sticker .tagline { color: #fff; font-weight: 700; font-style: italic; font-size: 13.5px; line-height: 17px; }
  .sticker .question { color: var(--navy); font-weight: 600; font-size: 14px; line-height: 18px; }
  .sticker .link { color: var(--navy); font-weight: 700; font-size: 9.5px; line-height: 14px; }
  .sticker .phone { position: absolute; left: 0; right: 0; top: 121px; font-size: 10px; }

  /* Envelope */
  .envelope { left: 517px; top: 529px; width: 623px; height: 311px; }
  .envelope .sender { position: absolute; left: 26px; top: 24px; font-size: 9.5px; line-height: 11px; }
  .envelope .wordmark { font-size: 23px; margin-bottom: 11px; }
  .envelope .wordmark .dot { width: 11px; height: 11px; }
  .envelope .stamp {
    position: absolute; left: 486px; top: 20px; width: 116px; height: 79px;
    background: linear-gradient(135deg, #2a8a92, var(--stamp) 55%, #164f57);
    outline: 2px dotted #fff; outline-offset: -1px;
  }
</style>
</head>
<body>

<section class="sheet letterhead">
  <div class="wordmark"><span class="dot"></span>Vikstrandbil</div>
  <footer class="footer">
    <p class="company">Vikstrandbil AS</p>
    <p><span class="label">Address:</span> 8613 Lysvær</p>
    <p><span class="label">Telefon:</span> 47283916&nbsp; <span class="label">Mail:</span> skips@vikstrand.no&nbsp; <span class="label">Web:</span> vikstrand.no</p>
    <p><span class="label">Org. nr:</span> 981 537 608</p>
  </footer>
</section>

<section class="sheet business-card">
  <div class="wordmark"><span class="dot"></span>Vikstrandbil</div>
  <p class="name">Leif Brattli</p>
  <div class="details">
    <p><span class="label">Telefon:</span> 47283916</p>
    <p><span class="label">Address:</span> 8613 Lysvær</p>
    <p><span class="label">Mail:</span> Leif@vikstrand.no&nbsp; <span class="label">Web:</span> vikstrand.no</p>
  </div>
</section>

<section class="sheet sticker">
  <div class="wordmark"><span class="dot"></span>Vikstrandbil</div>
  <div class="band">
    <p class="tagline">Fraktæ av Vikstrandbil.</p>
    <p class="question">Ke du syns?</p>
    <p class="link">Vikstrand.no/tilbakemelding</p>
  </div>
  <p class="phone"><span class="label">Telefon:</span> 47283916</p>
</section>

<section class="sheet envelope">
  <div class="sender">
    <div class="wordmark"><span class="dot"></span>Vikstrandbil</div>
    <p class="company">Vikstrandbil AS</p>
    <p><span class="label">Address:</span> 8613 Lysvær</p>
    <p><span class="label">Telefon:</span> 47283916</p>
    <p><span class="label">Org. nr:</span> 981 537 608</p>
  </div>
  <div class="stamp" role="img" aria-label="Norwegian postage stamp showing a fish swimming underwater"></div>
</section>

</body>
</html>
```